Need a business cards for a hair dressing salon.

Target Market(s)

Target woman for Hair cuts, bridal makeup, occasion, fashion makeup and etc.

Industry/Entity Type

Hair

Font styles to use
Serif
Script

Requirements
Must have
• - Business card to be memorable and recognizable

- Please include the following on the business card:
- Business name: Salon Marolin
- Name: Nilumi Jayasekara (Name Must be changeable)
- Occupation: Hair Dresser & Beautician
- Contact number: 04 731 6 CURL
- Email: mail@marolin.com.au
- Facebook (please use image): www.facebook.com/marolin.com.au
Nice to have
• Font Styles:
Business Name - Script
Other Text - Serif

```html
<!DOCTYPE html>
<html lang="en">
<head>
<meta charset="utf-8">
<title>Salon Marolin – Business Card</title>
<link href="https://fonts.googleapis.com/css2?family=Quicksand:wght@300;400;500&display=swap" rel="stylesheet">
<style>
  :root {
    --page-bg: #e9e6e3;
    --card-white: #ffffff;
    --salon-pink: #f0647f;
    --ink-dark: #3a2630;
    --dot-navy: #1f2450;
    --tool-dark: #1c1c24;
  }
  html, body {
    margin: 0;
    padding: 0;
    width: 1200px;
    height: 976px;
    overflow: hidden;
    background: var(--page-bg);
  }
  .canvas {
    position: relative;
    width: 1200px;
    height: 976px;
  }
  .business-card {
    position: absolute;
    left: 100px;
    top: 202px;
    width: 1000px;
    height: 572px;
    background: var(--card-white);
    box-shadow: 0 10px 30px rgba(0,0,0,0.18);
    overflow: hidden;
    font-family: "Quicksand", sans-serif;
  }
  .pink-band {
    position: absolute;
    left: 0;
    top: 46px;
    width: 100%;
    height: 344px;
    background: var(--salon-pink);
  }
  .bottom-stripe {
    position: absolute;
    left: 0;
    bottom: 0;
    width: 100%;
    height: 14px;
    background: var(--salon-pink);
  }
  .card-text {
    position: absolute;
    left: 34px;
    top: 62px;
    color: var(--card-white);
  }
  .salon-name {
    margin: 0 0 18px;
    font-size: 64px;
    font-weight: 300;
    letter-spacing: 1px;
    line-height: 1.1;
  }
  .stylist-name {
    margin: 0;
    font-size: 31px;
    font-weight: 400;
    color: var(--ink-dark);
    line-height: 1.05;
  }
  .contact-list {
    margin: 0;
    padding: 0;
    list-style: none;
    font-size: 30px;
    font-weight: 300;
    line-height: 1.0;
  }
  .scissors-mark {
    position: absolute;
    left: 26px;
    top: 330px;
    width: 150px;
    height: 120px;
    background: linear-gradient(135deg, var(--tool-dark), #3b3b46);
    border-radius: 10px;
  }
  .cut-line {
    position: absolute;
    left: 180px;
    top: 440px;
    width: 760px;
    height: 6px;
  }
</style>
</head>
<body>
  <main class="canvas">
    <article class="business-card">
      <div class="pink-band"></div>
      <div class="card-text">
        <h1 class="salon-name">Salon Marolin</h1>
        <p class="stylist-name">Nilumi Jayasekara</p>
        <ul class="contact-list">
          <li>Hair Dresser &amp; Beautician</li>
          <li>tel: 04 731 6 CURL</li>
          <li>email: mail@marolin.com.au</li>
          <li>fb: www.friendbook.com/marolin.com.au</li>
        </ul>
      </div>
      <div class="scissors-mark" role="img" aria-label="Scissors illustration cutting along the dotted line"></div>
      <svg class="cut-line" viewBox="0 0 760 6" aria-hidden="true">
        <line x1="3" y1="3" x2="757" y2="3" stroke="var(--dot-navy)" stroke-width="4" stroke-linecap="round" stroke-dasharray="0 14"/>
      </svg>
      <div class="bottom-stripe"></div>
    </article>
  </main>
</body>
</html>
```